Business Card & Logo Design

Originally the brief was for a card only - I now think it's probably better to include a logo design as well. PLease add $200 to the Budget of $210, Apologies for the inconvenience for thaos that have already submitted designs.

Lamp And Harbor Studios Pty Ltd is a video/dvd/ production company. Primarily corporate medium to high end. It's a one man operation that's been in business 20 years.

The name " Lamp and Harbor" is a primarily a reference to Lucien Marbeck film that's about film making. Shooting "Lamp and harbor" is also a technique employed by cinematographers to make scenes shot in daylight look like night.

See the design emphasising blue day/night tones but open to other ideas.

Main Text can either be Lamp and Harbor Studios or Lamp And Harbor.
Updates

Many thanks to all designers who submitted ideas for this brief.

Choosing between the designs was very difficult indeed.

I wish everyone the best and may the next job be yours!

Walter

Industry/Entity Type

Business

Requirements
Must have
• Text for card:
In Larger Print
Lamp And Harbor Studios or Lamp And Harbor
Walter Brenic
In Smaller Print
Lamp And Harbor Studios Pty Ltd.
17 Calder Lane
Fernwood, VIC, 3188
P: 9734 2061
m: 0417 385 902
e: walterbrenic@examplemail.net

```html
<!DOCTYPE html>
<html lang="en">
<head>
<meta charset="utf-8">
<title>Lamp and Harbor Studios – Business Card</title>
<link rel="stylesheet" href="https://fonts.googleapis.com/css2?family=Marcellus&family=Mr+Dafoe&display=swap">
<style>
  :root {
    --backdrop: #d9dadc;
    --card: #ffffff;
    --brand-blue: #2483c9;
    --ink: #2a2a2a;
  }
  * { margin: 0; padding: 0; box-sizing: border-box; }
  html, body {
    width: 1200px;
    height: 397px;
    overflow: hidden;
    background: var(--backdrop);
  }
  .canvas {
    position: relative;
    width: 1200px;
    height: 397px;
    background: var(--backdrop);
  }
  .card {
    position: absolute;
    top: 47px;
    width: 542px;
    height: 300px;
    background: var(--card);
    border-radius: 36px;
    overflow: hidden;
  }
  .card--front { left: 43px; }
  .card--back { left: 616px; }

  .brand-name {
    position: absolute;
    left: 0;
    width: 100%;
    text-align: center;
    font-family: "Marcellus", serif;
    font-size: 27px;
    line-height: 34px;
    color: var(--brand-blue);
    letter-spacing: 0.5px;
    white-space: nowrap;
  }
  .card--front .brand-name { top: 134px; }
  .card--back .brand-name { top: 57px; }

  .contact {
    position: absolute;
    left: 37px;
    top: 186px;
    font-family: "Marcellus", serif;
    font-size: 11px;
    line-height: 18.3px;
    font-variant: small-caps;
    color: var(--ink);
    list-style: none;
    white-space: nowrap;
  }
  .contact__company { font-weight: bold; letter-spacing: 0.3px; }
  .contact__label { font-weight: bold; }

  .signature-name {
    position: absolute;
    left: 300px;
    top: 208px;
    font-family: "Mr Dafoe", cursive;
    font-size: 36px;
    line-height: 40px;
    color: var(--ink);
    white-space: nowrap;
    transform: rotate(-13deg);
    transform-origin: left center;
  }
</style>
</head>
<body>
<main class="canvas">
  <section class="card card--front" aria-label="Card front">
    <h1 class="brand-name">Lamp and Harbor Studios</h1>
  </section>

  <section class="card card--back" aria-label="Card back">
    <p class="brand-name">Lamp and Harbor Studios</p>
    <ul class="contact">
      <li class="contact__company">Lamp And Harbor Studios Pty Ltd.</li>
      <li>17 Calder Lane, Fernwood, VIC, 3188</li>
      <li><span class="contact__label">P:</span> 9734 2061</li>
      <li><span class="contact__label">M:</span> 0417 385 902</li>
      <li><span class="contact__label">E:</span> walterbrenic@examplemail.net</li>
    </ul>
    <p class="signature-name">Walter Brenic</p>
  </section>
</main>
</body>
</html>
```